KPVT

We want to design our company brochure. We are a newly established ship management company in Singapore. We manage a fleet of bulk carrier and car carriers. Our job is to run the ships economically and efficiently on behalf of owners of the vessel.
Updates

Project Deadline Extended
Reason: We are not satisfied by the designs as yet. Hence, we are extending the deadline further by 7 days.

Project Deadline Extended
Reason: No designs are up to our expectations

Project Deadline Extended

Target Market(s)

Our target market is various ship owners based all over the world especially in Japan and Europe. These ship owners are looking for third party managers to run their ships economically and efficiently.

Industry/Entity Type

It Company

Colors
32b7a4
33a6d7
00a88f
3276b5
0692cd
86cae6
86cfc6
ebf7f9
edf2f7

Requirements
Must have
• The brochure must have four pages (in form of a folder) with static information, photographs etc with a pocket designed inside to keep printed sheets containing dynamic information.
Write up on our company is attached herewith and also some photographs depicting our ships, crew and the training center.
Information for dynamic sheets is attached in a separate sheets.

```html
<!DOCTYPE html>
<html lang="en">
<head>
<meta charset="utf-8">
<title>KPVT Brochure Spread</title>
<link href="https://fonts.googleapis.com/css2?family=Open+Sans:wght@400;600;700&display=swap" rel="stylesheet">
<style>
:root{
  --blue:#1f68ad;
  --blue-deep:#185a99;
  --green:#7ab648;
  --ink:#3d3d3d;
  --ink-soft:#555;
  --paper:#f7f8fa;
  --page-edge:#dfe3e8;
  --rule:#9aa3ad;
  --bg:#e9eaec;
  --tab-text:#ffffff;
}
*{box-sizing:border-box;margin:0;padding:0}
html,body{width:1200px;height:1000px;overflow:hidden}
body{background:var(--bg);font-family:"Open Sans",Arial,sans-serif;color:var(--ink);position:relative}
.spread{position:absolute;left:40px;top:104px;width:1120px;height:792px;display:flex;box-shadow:0 10px 30px rgba(0,0,0,.18)}
.page{position:relative;width:560px;height:792px;background:var(--paper);overflow:hidden}
.page--left{border-right:1px solid var(--page-edge)}
.band-top{position:absolute;left:0;top:0;width:100%;height:22px;background:var(--blue);border-bottom:3px solid var(--green)}
.band-bottom{position:absolute;left:0;bottom:0;width:100%;height:14px;background:var(--blue);border-top:3px solid var(--green)}
.frame-line{position:absolute;left:12px;top:22px;bottom:14px;width:3px;background:var(--blue)}
.page--right .frame-line{left:auto;right:12px}

.about{position:absolute;left:34px;top:46px;width:290px}
.heading{font-weight:700;color:var(--blue);font-size:22px;letter-spacing:.5px;margin-bottom:8px}
.about p{font-size:10.4px;line-height:1.42;color:var(--ink-soft);margin-bottom:9px;text-align:justify}

.photo-column{position:absolute;left:340px;top:46px;width:200px;display:flex;flex-direction:column;gap:8px}
.photo{display:block;border:3px solid #fff;box-shadow:0 1px 4px rgba(0,0,0,.2)}
.photo-column .photo{height:165px}
.ph-carrier{background:linear-gradient(180deg,#b9d3e6 0%,#dbe6ee 45%,#4f7aa3 100%)}
.ph-crew{background:linear-gradient(180deg,#f1f1f1 0%,#c8302c 45%,#d9d9d9 100%)}
.ph-bulk{background:linear-gradient(180deg,#c9d5df 0%,#8fa4b6 45%,#7b2326 75%,#8b8f93 100%)}
.ph-deck{background:linear-gradient(180deg,#54595e 0%,#7f8184 40%,#e0783c 60%,#3e4246 100%)}

.tab{position:absolute;display:inline-block;background:var(--blue);color:var(--tab-text);font-weight:600;text-transform:uppercase;letter-spacing:.5px;border-bottom:3px solid var(--green);clip-path:polygon(0 0,100% 0,96% 100%,0 100%)}
.services-tab{left:22px;top:466px;font-size:17px;padding:5px 30px 5px 14px}
.services{position:absolute;left:64px;top:512px;width:270px;border-left:1px solid var(--rule);padding-left:22px;padding-bottom:6px}
.services-main li,.services-sub li{list-style:none;position:relative}
.services-main li{font-size:15px;font-weight:600;color:var(--ink);margin-bottom:6px}
.services-main .tick{left:-50px;top:3px;width:16px;height:14px}
.services-tagline{font-size:14px;font-weight:600;color:var(--blue);line-height:1.25;margin:4px 0 8px}
.services-sub li{font-size:12.5px;font-weight:600;color:var(--ink);margin-bottom:4px;padding-left:22px}
.services-sub .tick{left:0;top:3px;width:13px;height:12px}
.tick{position:absolute;fill:none;stroke:var(--blue);stroke-width:3;stroke-linecap:round;stroke-linejoin:round}

.ph-office{position:absolute;left:30px;top:42px;width:498px;height:200px;background:linear-gradient(90deg,#e9eef2 0%,#d7cfc5 40%,#8c5b46 70%,#ede7e2 100%)}
.initiatives-tab{left:28px;top:260px;font-size:15px;padding:4px 34px 4px 14px}
.initiatives{position:absolute;left:36px;top:298px;width:490px}
.initiatives li{list-style:none;position:relative;padding-left:24px;font-size:10.8px;line-height:1.38;color:var(--ink-soft);margin-bottom:5px}
.initiatives .tick{left:0;top:3px;width:13px;height:12px}

.commitment{position:absolute;left:22px;right:26px;top:512px;bottom:14px;background:var(--blue-deep);border-top-left-radius:28px;border-top:3px solid var(--green);padding:30px 250px 0 24px;color:#fff}
.commitment .heading{color:#fff;font-size:22px}
.commitment p{font-size:11px;line-height:1.5;text-align:justify;color:#e3eef8}
.ph-ship-quay{position:absolute;right:30px;top:492px;width:214px;height:184px;background:linear-gradient(180deg,#b7c6d3 0%,#cfd8df 35%,#1e1e22 60%,#a5312b 78%,#8a8d90 100%)}
</style>
</head>
<body>
<svg width="0" height="0" style="position:absolute" aria-hidden="true">
  <symbol id="tick" viewBox="0 0 16 14"><path d="M2 7.5 6 12 14 2"/></symbol>
</svg>

<div class="spread">
  <section class="page page--left">
    <div class="band-top"></div>
    <div class="frame-line"></div>

    <div class="about">
      <h2 class="heading">ABOUT US</h2>
      <p>Kestrel Pacific Vessel Technical Pte. Ltd, established in Singapore in 2012 as a Ship Management company with a clear objective to provide quality service to the Ship Owners while maintaining a fine balance and harmony between cost, efficient operation and giving a humane touch to the Ship Management.</p>
      <p>With this philosophy, Kestrel Pacific Vessel Technical Pte. Ltd was formed and was chosen as a dependable ally by Harumi Maritime Group who have trusted us for the upkeep and safe operation of their ships for majority of their existing fleet and all new building vessels.</p>
      <p>We have a vision – to contribute to the ship management business its lost pride and glory by running Clean, Safe and Happy Ships ethically.</p>
      <p>Company is headed by Mr. Arun Mehta who has more than 20 years of sea and shore based experience in various positions in the Shipping industry with majority of time spent ashore in key management position. KPVT is his brainchild and a reflection of his youthful and energetic persona. Like minded professionals were chosen right from the inception who have become the corner stones of the organization to build a strong yet dynamic entity.</p>
    </div>

    <div class="photo-column">
      <div class="photo ph-carrier" role="img" aria-label="Car carrier vessel at sea"></div>
      <div class="photo ph-crew" role="img" aria-label="Crew in red survival suits lined up on deck"></div>
      <div class="photo ph-bulk" role="img" aria-label="Bulk carrier berthed at port"></div>
      <div class="photo ph-deck" role="img" aria-label="Crew in safety gear working inside a car deck"></div>
    </div>

    <div class="tab services-tab">Services Offered</div>
    <div class="services">
      <ul class="services-main">
        <li><svg class="tick"><use href="#tick"/></svg>Ship Management</li>
        <li><svg class="tick"><use href="#tick"/></svg>Technical Solutions</li>
      </ul>
      <p class="services-tagline">An array of technical solutions for the shipping world</p>
      <ul class="services-sub">
        <li><svg class="tick"><use href="#tick"/></svg>Technical Consultancy</li>
        <li><svg class="tick"><use href="#tick"/></svg>New Building Supervision</li>
        <li><svg class="tick"><use href="#tick"/></svg>Pre-Purchase Surveys</li>
        <li><svg class="tick"><use href="#tick"/></svg>On-Site Supervision</li>
        <li><svg class="tick"><use href="#tick"/></svg>Dry Docking</li>
        <li><svg class="tick"><use href="#tick"/></svg>Condition Surveys</li>
        <li><svg class="tick"><use href="#tick"/></svg>Port Captaincy</li>
      </ul>
    </div>

    <div class="band-bottom"></div>
  </section>

  <section class="page page--right">
    <div class="band-top"></div>
    <div class="frame-line"></div>

    <div class="photo ph-office" role="img" aria-label="Office corridor of the representative office"></div>

    <div class="tab initiatives-tab">Initiatives</div>
    <ul class="initiatives">
      <li><svg class="tick"><use href="#tick"/></svg>Started own in house training institute in Manila to train our staff and keep them abreast of new developments in shipping industry.</li>
      <li><svg class="tick"><use href="#tick"/></svg>ECDIS installation started on board in order to ensure smooth transition to paperless navigation with proper training to ship staff in our training center.</li>
      <li><svg class="tick"><use href="#tick"/></svg>Commenced Internet facility on board all our vessels. 20 mb data being given free to each crew every month.</li>
      <li><svg class="tick"><use href="#tick"/></svg>Special emphasis on crew welfare with supply of fitness and entertainment equipment on board.</li>
      <li><svg class="tick"><use href="#tick"/></svg>Assistance like free telephone cards, internet cards, cash donation provided to staff in case of a natural calamity in home country.</li>
    </ul>

    <div class="commitment">
      <h2 class="heading">COMMITMENT</h2>
      <p>The company believes that good training, motivation and emphasis on human values are essential for long term success. Consequently, the company is committed to providing an ideal working environment both in its offices and on ships.</p>
    </div>
    <div class="photo ph-ship-quay" role="img" aria-label="Bulk carrier alongside a quay with cranes"></div>

    <div class="band-bottom"></div>
  </section>
</div>
</body>
</html>
```